fun theme dental practice website!

This client LOVES their superhero theme! They are an established pediatric dental practice with multiple locations. They have recently expanded to see adults and do orthodontics. They would like to have a new website design for the adult part of their practice. It should be similar in theme (superhero) but more adult (no sugarbugs!) . Navigation: about, meet the team, treatments, orthodontics, contact
add appointment request feature

Target Market(s)

adults

Industry/Entity Type

Dental

Number of Pages Required

2 page

Requirements
Must have
• home page design and interior page design
• fun and in theme but not too babyish (should it still look like a comic book?)
• appointment request feature
• visual pow
• colors consistent with logo (see attached)
• use the tooth social media icons

```html
<!DOCTYPE html>
<html lang="en">
<head>
<meta charset="utf-8">
<title>Valor Dental</title>
<link rel="stylesheet" href="https://fonts.googleapis.com/css2?family=Bangers&family=Comic+Neue:wght@400;700&display=swap">
<style>
:root{
  --blue:#3f5aa8;
  --navy:#2d3e50;
  --slate:#4a5868;
  --yellow:#ffe600;
  --red:#fd3a45;
  --green:#7dcc3f;
  --green-dark:#5ea82a;
  --white:#ffffff;
}
*{box-sizing:border-box;margin:0;padding:0}
html,body{width:673px;height:1200px;overflow:hidden}
body{position:relative;background:var(--navy);font-family:"Comic Neue",cursive;color:var(--white)}
.abs{position:absolute}
.display{font-family:"Bangers",cursive;letter-spacing:.5px;font-style:italic;font-weight:400}
.hero{left:0;top:0;width:673px;height:348px;background:var(--blue)}
.brand{font-family:"Bangers",cursive;color:var(--yellow);font-size:21px;letter-spacing:.6px;line-height:1;white-space:nowrap}
.header-brand{left:45px;top:13px}
.nav{top:19px;left:0;width:673px;height:14px;font-family:"Bangers",cursive;font-size:9.5px;font-style:italic;letter-spacing:.4px;white-space:nowrap}
.nav a{position:absolute;top:0;color:var(--white);text-decoration:none}
.nav a.active{color:var(--red)}
.social{display:flex;gap:5px}
.social span{width:17px;height:19px;border-radius:50%;background:var(--red);display:block}
.header-social{left:524px;top:13px}
.arrow{width:28px;height:35px;background:var(--red);top:156px}
.arrow svg{display:block;margin:9px auto}
.arrow-left{left:0}
.arrow-right{left:646px}
.hero-title{left:72px;top:112px;font-size:23px;line-height:27px;color:var(--yellow);white-space:nowrap}
.hero-title em{color:var(--red);font-style:inherit}
.copy{font-size:8.2px;line-height:14px}
.hero-copy{left:70px;top:182px;width:262px}
.btn{display:block;width:114px;height:24px;background:var(--green);border-bottom:2px solid var(--green-dark);border-radius:2px;font-family:"Bangers",cursive;font-style:italic;font-size:11.5px;letter-spacing:.5px;line-height:23px;text-align:center;color:var(--white);text-decoration:none}
.btn-small{width:93px}
.hero-photo{left:350px;top:80px;width:250px;height:268px;border-radius:125px 125px 0 0;background:linear-gradient(180deg,#c99a7a,#e9d4c6 60%,#dfe3ea)}
.feature{width:184px;top:322px}
.feature-head{height:49px;background:var(--yellow);display:flex;align-items:center;gap:10px;padding-left:14px;box-shadow:3px -3px 0 var(--navy)}
.feature-head h2{font-family:"Bangers",cursive;font-style:italic;font-size:19px;color:var(--red);font-weight:400;letter-spacing:.5px;white-space:nowrap}
.feature .copy{margin-top:15px;width:188px}
.feature .btn{margin-top:16px}
.promo{left:45px;top:523px;width:583px;height:204px;background:var(--red)}
.promo-title{left:26px;top:22px;font-size:23px;line-height:27px;white-space:nowrap}
.promo-copy{left:25px;top:89px;width:280px}
.promo-btn{left:25px;top:155px}
.promo-photo{left:333px;top:25px;width:224px;height:155px;background:linear-gradient(120deg,#f3eee9,#d9a78b 55%,#f4ede8)}
.team-title{left:0;top:743px;width:673px;text-align:center;font-size:24px;color:var(--yellow)}
.member{top:789px;width:184px;height:219px;background:var(--slate);text-align:center}
.avatar{width:64px;height:64px;border-radius:50%;border:3px solid var(--navy);margin:22px auto 0;background:linear-gradient(180deg,#c9d3de,#f1e7e0)}
.member h3{font-family:"Bangers",cursive;font-style:italic;font-weight:400;font-size:11px;color:var(--yellow);margin-top:11px;letter-spacing:.4px}
.member .copy{padding:0 12px;margin-top:2px}
.member .btn{margin:12px auto 0}
.footer{left:0;top:1032px;width:673px;height:168px;background:var(--blue)}
.footer-brand{left:45px;top:24px}
.footer-copy{left:46px;top:66px;width:170px}
.follow{left:45px;top:105px;display:flex;align-items:center;gap:10px}
.follow b{font-family:"Bangers",cursive;font-style:italic;font-weight:400;color:var(--yellow);font-size:10px;letter-spacing:.4px}
.col{top:19px}
.col h4{font-family:"Bangers",cursive;font-style:italic;font-weight:400;color:var(--yellow);font-size:10.5px;letter-spacing:.4px;margin-bottom:6px}
.col li{list-style:none;font-size:8.2px;line-height:14px;white-space:nowrap}
.contact li{display:flex;gap:8px}
.contact svg{flex:none;margin-top:3px}
.legal{left:0;top:150px;width:673px;text-align:center;font-size:8.2px}
</style>
</head>
<body>
<section class="hero abs">
  <div class="header-brand brand abs">Valor Dental</div>
  <nav class="nav abs">
    <a class="active" href="#" style="left:162px">Home</a><a href="#" style="left:203px">About Us</a><a href="#" style="left:257px">Meet the Team</a><a href="#" style="left:332px">Treatments</a><a href="#" style="left:396px">Orthodontics</a><a href="#" style="left:470px">Contact Us</a>
  </nav>
  <div class="header-social social abs" aria-label="Social links"><span></span><span></span><span></span><span></span><span></span></div>
  <div class="arrow arrow-left abs"><svg width="12" height="16" viewBox="0 0 12 16"><path d="M9 2L3 8l6 6" stroke="#fff" stroke-width="3" fill="none"/></svg></div>
  <div class="arrow arrow-right abs"><svg width="12" height="16" viewBox="0 0 12 16"><path d="M3 2l6 6-6 6" stroke="#fff" stroke-width="3" fill="none"/></svg></div>
  <div class="hero-photo abs" role="img" aria-label="Smiling woman resting her chin on her hand"></div>
  <h1 class="hero-title display abs">Providing complete <em>dental</em><br>and <em>oral care</em></h1>
  <p class="hero-copy copy abs">Lorem ipsum dolor sit amet, eum velit timeam mel vide numquam ponderm. Mollis scaevola in sint dicta nec, agam esse tollit quo id praesent eu onequ untures magni dolores eonemo eniptai volupta equi nesciunt ades.</p>
  <a class="btn abs" style="left:70px;top:246px" href="#">Set an appointment</a>
</section>

<article class="feature abs" style="left:45px">
  <div class="feature-head"><svg width="34" height="34" viewBox="0 0 34 34"><circle cx="17" cy="17" r="15" fill="none" stroke="#fd3a45" stroke-width="3"/><path d="M11 11c2-2 4-1 6 0 2-1 4-2 6 0 2 3 0 7-1 9l-1 5c-1 1-2 0-2-1l-1-4h-2l-1 4c0 1-1 2-2 1l-1-5c-1-2-3-6-1-9z" fill="#fd3a45"/></svg><h2>Our Profile</h2></div>
  <p class="copy">Lorem ipsum dolor sit amet, eum velit timeam mel vide numquam ponderm. Mollis scaevola in sint dict nec, agam esse tollit quo id prasent eu onequ amet untures magni dolores eonemon eniptai volupta sit equi nesciunt ades.</p>
  <a class="btn btn-small" href="#">Read more</a>
</article>
<article class="feature abs" style="left:244px">
  <div class="feature-head"><svg width="34" height="34" viewBox="0 0 34 34"><circle cx="17" cy="17" r="15" fill="none" stroke="#fd3a45" stroke-width="3"/><path d="M11 25l11-13" stroke="#fd3a45" stroke-width="3" stroke-linecap="round"/><rect x="19" y="7" width="6" height="7" rx="1" transform="rotate(40 22 10)" fill="#fd3a45"/></svg><h2>Care Advice</h2></div>
  <p class="copy">Lorem ipsum dolor sit amet, eum velit timeam mel vide numquam ponderm. Mollis scaevola in sint dict nec, agam esse tollit quo id prasent eu onequ amet untures magni dolores eonemon eniptai volupta sit equi nesciunt ades.</p>
  <a class="btn btn-small" href="#">Read more</a>
</article>
<article class="feature abs" style="left:444px">
  <div class="feature-head"><svg width="34" height="34" viewBox="0 0 34 34"><circle cx="17" cy="17" r="15" fill="none" stroke="#fd3a45" stroke-width="3"/><rect x="9" y="12" width="16" height="12" rx="2" fill="#fd3a45"/><rect x="14" y="9" width="6" height="4" fill="none" stroke="#fd3a45" stroke-width="2"/><path d="M17 14v8M13 18h8" stroke="#ffe600" stroke-width="2.4"/></svg><h2>Emergencies</h2></div>
  <p class="copy">Lorem ipsum dolor sit amet, eum velit timeam mel vide numquam ponderm. Mollis scaevola in sint dict nec, agam esse tollit quo id prasent eu onequ amet untures magni dolores eonemon eniptai volupta sit equi nesciunt ades.</p>
  <a class="btn btn-small" href="#">Read more</a>
</article>

<section class="promo abs">
  <h2 class="promo-title display abs">Providing complete<br>orthodontics solutions</h2>
  <p class="promo-copy copy abs">Lorem ipsum dolor sit amet, eum velit timeam mel vide numquam ponderm. Mollis scaevola in sint dicta nec, agam esse tollit quo id praesent eu onequ untures magni dolores eonemo eniptai volupta equi nesciunt ades.</p>
  <a class="promo-btn btn abs" href="#">Set an appointment</a>
  <div class="promo-photo abs" role="img" aria-label="Close-up of a smile with dental braces"></div>
</section>

<h2 class="team-title display abs">Meet our team</h2>
<article class="member abs" style="left:45px">
  <div class="avatar" role="img" aria-label="Portrait of Dr. Nora Whitfield"></div>
  <h3>Dr. Nora Whitfield</h3>
  <p class="copy">Lorem ipsum dolor sit amet, eum velit time videm numquam ponderm. Mollis scaevola in sint amet dict nec agam esse tollit quo.</p>
  <a class="btn btn-small" href="#">Read more</a>
</article>
<article class="member abs" style="left:244px">
  <div class="avatar" role="img" aria-label="Portrait of Dr. Marcus Pell"></div>
  <h3>Dr. Marcus Pell</h3>
  <p class="copy">Lorem ipsum dolor sit amet, eum velit time videm numquam ponderm. Mollis scaevola in sint amet dict nec agam esse tollit quo.</p>
  <a class="btn btn-small" href="#">Read more</a>
</article>
<article class="member abs" style="left:444px">
  <div class="avatar" role="img" aria-label="Portrait of Dr. Ines Carrow"></div>
  <h3>Dr. Ines Carrow</h3>
  <p class="copy">Lorem ipsum dolor sit amet, eum velit time videm numquam ponderm. Mollis scaevola in sint amet dict nec agam esse tollit quo.</p>
  <a class="btn btn-small" href="#">Read more</a>
</article>

<footer class="footer abs">
  <div class="footer-brand brand abs">Valor Dental</div>
  <p class="footer-copy copy abs">Consectetur adipisci velit, sed quia numquam non eius modi tempordunt,</p>
  <div class="follow abs"><b>Follow us :</b><div class="social"><span></span><span></span><span></span><span></span><span></span></div></div>
  <div class="col abs" style="left:246px"><h4>Quick Links</h4><ul><li>Home</li><li>About US</li><li>Meet the Team</li><li>Treatments</li><li>Orthodontics</li><li>Contact</li></ul></div>
  <div class="col abs" style="left:361px"><h4>Quick Links</h4><ul><li>Our Profile</li><li>Care &amp; Advices</li><li>Emergencies</li><li>FAQs</li><li>Terms &amp; Conditions</li><li>Privacy Policy</li></ul></div>
  <div class="col contact abs" style="left:475px"><h4>Contact Us</h4><ul>
    <li><svg width="9" height="8" viewBox="0 0 9 8"><path d="M4.5 0L9 4H7.5v4h-2V5.5h-2V8h-2V4H0z" fill="#ffe600"/></svg><span>415 Harbor Ave Ste 210, Lakeview<br>IL 60999-0000</span></li>
    <li style="margin-top:2px"><svg width="9" height="7" viewBox="0 0 9 7"><rect width="9" height="7" fill="#ffe600"/><path d="M0 0l4.5 4L9 0" stroke="#3f5aa8" fill="none"/></svg><span>hello@valordental.test</span></li>
    <li style="margin-top:2px"><svg width="9" height="9" viewBox="0 0 9 9"><path d="M1 1l2-1 1 2-1 1c1 2 2 3 3 3l1-1 2 1-1 2C4 8 1 5 1 1z" fill="#ffe600"/></svg><span>+100 555 01234</span></li>
  </ul></div>
  <p class="legal abs">Demo © 2016 Privacy Policy. All Rights Reserved.</p>
</footer>
</body>
</html>
```